landscape and garden design business card

I would like a business card designed for my landscape and garden design company, Wrenfield Landscapes. We are located in Colorado. I would like to include our logo, contact info, and social media/web site address or QR code. Looking for an organic, flowing design that incorporates our logo.

Target Market(s)

Homeowners and businesses that need garden and landscape design

Contact Information for Business Card

Would like it to say landscape and garden design

Requirements
Must have
• Landscape and garden design

```html
<!DOCTYPE html>
<html lang="en">
<head>
<meta charset="utf-8">
<title>Wrenfield Landscapes – Business Card</title>
<link href="https://fonts.googleapis.com/css2?family=Montserrat:wght@400;500;700&display=swap" rel="stylesheet">
<style>
  :root {
    --bg-top: #4a4a4a;
    --bg-bottom: #1c1c1c;
    --forest: #03292a;
    --forest-light: #0c3d3d;
    --stone: #c2c3ba;
    --ink: #0a2b2b;
    --paper: #ffffff;
  }
  * { margin: 0; padding: 0; box-sizing: border-box; }
  html, body { width: 1200px; height: 875px; overflow: hidden; }
  body {
    background: linear-gradient(160deg, var(--bg-top), var(--bg-bottom));
    font-family: "Montserrat", sans-serif;
    position: relative;
  }
  .card {
    position: absolute;
    width: 540px;
    height: 308px;
    border-radius: 18px;
    overflow: hidden;
    box-shadow: 0 18px 40px rgba(0,0,0,0.45);
  }
  /* Front */
  .card-front {
    left: 330px; top: 90px;
    background: linear-gradient(100deg, var(--forest-light) 0%, var(--forest) 35%, var(--forest) 100%);
    display: flex; flex-direction: column; align-items: center; justify-content: center;
    gap: 18px;
  }
  .front-mark {
    width: 120px; height: 120px; border-radius: 50%;
    background: var(--stone);
  }
  .front-name {
    color: var(--stone);
    font-weight: 500;
    font-size: 30px;
    letter-spacing: 1px;
    text-align: center;
    line-height: 1.15;
  }
  /* Back */
  .card-back {
    left: 330px; top: 478px;
    background: var(--paper);
  }
  .back-band {
    position: absolute; left: 0; right: 0; bottom: 0; height: 22px;
    background: var(--forest);
  }
  .back-brand {
    position: absolute; left: 30px; top: 60px; width: 200px;
    display: flex; flex-direction: column; align-items: center; gap: 14px;
  }
  .back-mark {
    width: 104px; height: 104px; border-radius: 50%;
    background: var(--forest);
  }
  .back-name {
    color: var(--ink);
    font-weight: 500;
    font-size: 22px;
    text-align: center;
    line-height: 1.15;
  }
  .divider {
    position: absolute; left: 252px; top: 58px; width: 1.5px; height: 170px;
    background: var(--ink);
  }
  .contact {
    position: absolute; left: 274px; top: 56px; right: 20px;
    color: var(--ink);
  }
  .contact-name { font-weight: 700; font-size: 22px; }
  .contact-title { font-size: 12px; margin-top: 2px; }
  .contact-address { font-size: 12.5px; margin-top: 14px; line-height: 1.35; }
  .contact-list { list-style: none; margin-top: 14px; font-size: 12.5px; }
  .contact-list li { display: flex; align-items: center; gap: 8px; margin-bottom: 5px; }
  .contact-list svg { width: 12px; height: 12px; fill: var(--ink); flex: none; }
</style>
</head>
<body>
  <section class="card card-front">
    <div class="front-mark" role="img" aria-label="Wrenfield Landscapes emblem"></div>
    <div class="front-name">Wrenfield Landscapes</div>
  </section>

  <section class="card card-back">
    <div class="back-brand">
      <div class="back-mark" role="img" aria-label="Wrenfield Landscapes emblem"></div>
      <div class="back-name">Wrenfield Landscapes</div>
    </div>
    <div class="divider"></div>
    <div class="contact">
      <div class="contact-name">Clara Whitmore</div>
      <div class="contact-title">Owner/Landscape and Garden Design</div>
      <div class="contact-address">418 Aspen Ridge Ln. #12<br>Boulder, CO 80302</div>
      <ul class="contact-list">
        <li><svg viewBox="0 0 24 24"><path d="M6.6 10.8a15 15 0 0 0 6.6 6.6l2.2-2.2a1 1 0 0 1 1-.25 11.4 11.4 0 0 0 3.6.57 1 1 0 0 1 1 1V20a1 1 0 0 1-1 1A17 17 0 0 1 3 4a1 1 0 0 1 1-1h3.5a1 1 0 0 1 1 1c0 1.25.2 2.45.57 3.57a1 1 0 0 1-.25 1z"/></svg>303-555-0148</li>
        <li><svg viewBox="0 0 24 24"><path d="M2 5h20v14H2zm2 2v.5l8 5 8-5V7l-8 5z"/></svg>info@wrenfield.com</li>
        <li><svg viewBox="0 0 24 24"><circle cx="12" cy="12" r="10"/></svg>www.wrenfield.com</li>
      </ul>
    </div>
    <div class="back-band"></div>
  </section>
</body>
</html>
```